Flyer-Design für Unterstützung bei Organisation
Zielgruppe
Ich begleite und unterstütze Organisationen und Menschen in Organisationen in ihren Veränderungs- Entwicklungs- und Problemlösungsprozessen ( Führungscoaching, Teamcoaching, Teamentwicklung). Meine Zielgruppe sind Personen in den Berufsrollen Geschäftsführer, HR-Verantwortliche, Führungspersonen, Mitarbeitende in Firmen.
Aufgabenstellung
Ich möchte die Flyer in einem Briefversan mitsenden, wo ich Firmen anschreibe und meine Dienstleistungen vorstelle. Auch möchte ich den Flyer an Orten auflegen, wo mein Zielpublikum Konsultationen in Anspruch nehmen könnte, bsp. Versicherungsagenturen, Hausarztpraxis, Physiotherapie etc.
kurz, interessant und ansprechend die Dienstleistungen gemäss Homepage beschreiben
https://www.lumowegweis.ch/firmen
DIN-Format: DIN A6/5 210 x 105 mm ist optional, lasse mich gerne auch von anderen Vorschlägen überraschen.

```html
<!DOCTYPE html>
<html lang="de">
<head>
<meta charset="utf-8">
<title>Lumowegweis – Flyer</title>
<link href="https://fonts.googleapis.com/css2?family=Open+Sans:wght@400;600;700&display=swap" rel="stylesheet">
<style>
  :root {
    --brand-blue: #3a76a2;
    --brand-navy: #27306a;
    --sky-light: #a3d0f0;
    --sky-mid: #8cc0e8;
    --cloud-grey: #6b7584;
    --ink: #1e1e1e;
    --paper: #ffffff;
    --backdrop: #eceef1;
    --wordmark-grey: #8a8a8a;
  }
  * { box-sizing: border-box; margin: 0; padding: 0; }
  html, body {
    width: 1200px; height: 1157px; overflow: hidden;
    background: var(--backdrop);
    font-family: "Open Sans", Arial, sans-serif;
    color: var(--ink);
  }
  .flyer {
    position: absolute; left: 60px; width: 1080px; height: 520px;
    background: var(--paper); overflow: hidden;
    box-shadow: 0 6px 18px rgba(0,0,0,0.12);
  }
  .flyer--front { top: 40px; }
  .flyer--back { top: 597px; }

  .brand {
    position: absolute; left: 44px; top: 34px; z-index: 2;
    display: flex; align-items: center; gap: 12px;
  }
  .brand__dot { width: 26px; height: 26px; border-radius: 50%; background: var(--brand-blue); }
  .brand__name {
    font-size: 30px; font-weight: 600; letter-spacing: 1px;
    color: var(--wordmark-grey); text-transform: uppercase;
  }

  .footer-band {
    position: absolute; left: 0; right: 0; bottom: 0; height: 24px;
    background: var(--brand-blue);
  }

  /* front */
  .sky-photo {
    position: absolute; left: 0; right: 0; top: 112px; height: 232px;
    background: linear-gradient(180deg, var(--sky-light), var(--sky-mid));
  }
  .services {
    position: absolute; left: 0; right: 0; top: 206px;
    display: grid; grid-template-columns: repeat(4, 1fr);
  }
  .service { text-align: center; padding: 0 12px; }
  .service__badge {
    width: 150px; height: 150px; border-radius: 50%;
    background: var(--brand-blue); margin: 0 auto 12px;
  }
  .service__title {
    font-size: 20px; font-weight: 700; color: var(--brand-blue);
    text-transform: uppercase; letter-spacing: 0.3px; margin-bottom: 2px;
  }
  .service__text { font-size: 15.5px; line-height: 1.3; hyphens: auto; -webkit-hyphens: auto; }

  /* back */
  .road-photo {
    position: absolute; left: 0; right: 0; top: 130px; height: 232px;
    background: linear-gradient(90deg, var(--cloud-grey) 0%, #4a5877 45%, var(--brand-navy) 100%);
  }
  .signs-photo {
    position: absolute; left: 400px; top: 18px; width: 500px; height: 344px;
    border-radius: 40px; z-index: 1;
    background: radial-gradient(circle at 50% 55%, #3b4488 0%, var(--brand-navy) 70%);
  }
  .intro {
    position: absolute; left: 46px; top: 382px; width: 560px;
    font-size: 18px; font-weight: 600; line-height: 1.35; color: var(--brand-blue);
  }
  .contact {
    position: absolute; left: 700px; top: 372px; width: 360px;
    font-size: 16px; line-height: 1.35;
  }
  .contact__title {
    font-size: 20px; font-weight: 700; color: var(--brand-blue);
    text-transform: uppercase; margin-bottom: 2px;
  }
  .contact__row { display: flex; align-items: center; gap: 6px; }
  .contact__row svg { width: 15px; height: 15px; fill: none; stroke: var(--brand-blue); stroke-width: 2; }
  .contact__gap { margin-left: 14px; }
  .contact__web { font-weight: 700; color: var(--brand-blue); }
</style>
</head>
<body>

<section class="flyer flyer--front">
  <div class="brand"><span class="brand__dot"></span><span class="brand__name">Lumowegweis</span></div>
  <div class="sky-photo" role="img" aria-label="Foto: Vögel fliegen am blauen Himmel"></div>
  <div class="services">
    <article class="service">
      <div class="service__badge" role="img" aria-label="Symbol Businesscoaching"></div>
      <h2 class="service__title">Businesscoaching</h2>
      <p class="service__text">Bewusst Führen, die eigene Rolle reflektieren und/oder Probleme lösen.</p>
    </article>
    <article class="service">
      <div class="service__badge" role="img" aria-label="Symbol Teamcoaching"></div>
      <h2 class="service__title">Teamcoaching</h2>
      <p class="service__text">Im Team zusammenfinden, moti&shy;vierte und leistungsfähige Teams haben und/oder Konflikte lösen.</p>
    </article>
    <article class="service">
      <div class="service__badge" role="img" aria-label="Symbol Prozessoptimierung"></div>
      <h2 class="service__title">Prozessoptimierung</h2>
      <p class="service__text">Prozesse hinterfragen, doku&shy;mentieren, optimieren und mitgestalten.</p>
    </article>
    <article class="service">
      <div class="service__badge" role="img" aria-label="Symbol Stressmanagement"></div>
      <h2 class="service__title">Stressmanagement</h2>
      <p class="service__text">Die eigenen Stressfaktoren kennen, angehen und Wider&shy;standsfähiger werden.</p>
    </article>
  </div>
  <div class="footer-band"></div>
</section>

<section class="flyer flyer--back">
  <div class="road-photo" role="img" aria-label="Foto: bewölkter Himmel"></div>
  <div class="signs-photo" role="img" aria-label="Foto: sternförmig angeordnete Einbahnstrassen-Schilder"></div>
  <div class="brand"><span class="brand__dot"></span><span class="brand__name">Lumowegweis</span></div>
  <p class="intro">Ob Einzelpersonen oder Teams,<br>Sie erhalten eine professionelle Begleitung und Unterstützung in Ihren Veränderungs-, Entwicklungs- und Problemlösungsprozessen.</p>
  <div class="contact">
    <h2 class="contact__title">Kontaktieren Sie mich!</h2>
    <p>Lumowegweis - Carla Wyssmüller</p>
    <p>Talgasse 17, 3365 Birkental</p>
    <p class="contact__row">
      <svg viewBox="0 0 24 24"><path d="M5 3h4l2 5-3 2a12 12 0 0 0 6 6l2-3 5 2v4a2 2 0 0 1-2 2A17 17 0 0 1 3 5a2 2 0 0 1 2-2z"/></svg>
      079 000 12 34
      <svg class="contact__gap" viewBox="0 0 24 24"><path d="M22 2 2 10l8 3 3 8z M22 2 10 13"/></svg>
      info@lumowegweis.ch
    </p>
    <p class="contact__web">www.lumowegweis.ch</p>
  </div>
  <div class="footer-band"></div>
</section>

</body>
</html>
```